Tor Ridge Wine Club-The Onyx Roll

We are a new aspirational brand of fine Tasmania Wine. We need a commitment club poster which appeals to the ego.We have one opportunity to get customers to sign up and that is when they visit at the cellar door. This club is the core of our business.

The brand is a clean, pure , simple brand, black and white very sophiscated.
This is a top end product.

Our Commitment Club is named The Onyx Roll which is a play on words. Tradionally The Onyx Roll is a list of people that you dont want to do business with. So we are turning this on its had.

You need to make this poster sharp, desirable, possibly sexy but masculine. Im thinking Felix Crane . It doesnt matter the client will be 40 up fashion consious looking for something new , exclusive , something there peers don't have.

I dont like busy! make it clean clear and basically undeniable. The client must not be able to resist the offer.

www.torridgevines.com.au

Reason: Internet problems so cant get to respond and offer comment in a timely manner

Appreciator 40-60 male wants to be recognised fashion consious sophiscated has money and wants to part of something exclusive.

A feeling that you are part of something that only a few are. Exclusive

Maybe an imagine of beautiful people 30/40ish I want to be drinking Tor Wine / in The Onyx Roll

Fashion

Must have
• Tor Ridge Logo
TOR Bottles images

We produce only 1600 cases of wine each vintage. Therefore we have limited membership 001-999 for our club.
Award Winning Wines available exclusively from us.

Gold Member
We will reserve 2 cases of our limited vintage, to be delivered to you in May and Oct.
Single varietal or mixed cases. You receive a 15% discount.

Silver Member
We will reserve 1 case of our limited vintage to be delivered to you 6 bottles in May and 6 in Oct.
Single varietal or mixed cases. You receive a 10% discount.

To you exclusively from us not, available from any other retailers.

You will be invited to Onyx Roll Only Events and Tastings.
You will get preferential access to new and limited releases.
Members will be entered in a bi annual draw to win a 2 night stay here at the Tor Weavers Cottage on the Freycinet Coast Tasmania.

• VIP stamps,gimacs, anything that cheapens our brand.

We do not like busy posters please have white space

```html
<!DOCTYPE html>
<html lang="en">
<head>
<meta charset="utf-8">
<title>The Onyx Roll – Tor Ridge Wine Club</title>
<link rel="stylesheet" href="https://fonts.googleapis.com/css2?family=Oswald:wght@200;300;400;600&family=Arimo:wght@400;700&display=swap">
<style>
  :root {
    --backdrop: #e4e4e4;
    --paper: #ffffff;
    --onyx: #0b0b0b;
    --gold: #c7a566;
    --gold-deep: #a8864a;
    --ink-light: #f4f4f4;
    --ink-muted: #cfcfcf;
    --ink-dark: #1a1a1a;
  }
  * { box-sizing: border-box; margin: 0; padding: 0; }
  html, body {
    width: 1161px; height: 1200px; overflow: hidden;
    background: var(--backdrop);
  }
  .poster {
    position: absolute; left: 157px; top: 0;
    width: 846px; height: 1200px;
    background: var(--paper);
    overflow: hidden;
  }
  .banner-shape { position: absolute; left: 0; top: 0; }
  .banner {
    position: absolute; left: 52px; top: 0; width: 742px;
    color: var(--ink-light);
    font-family: "Oswald", sans-serif;
    text-align: center;
  }
  .ribbon {
    position: absolute; left: 243px; top: 58px; width: 256px; height: 30px;
  }
  .ribbon-label {
    position: absolute; left: 0; top: 0; width: 256px; height: 30px;
    line-height: 30px; font-size: 15px; font-weight: 400;
    letter-spacing: 6px; color: var(--onyx); text-transform: uppercase;
  }
  .title {
    position: absolute; left: 0; top: 104px; width: 742px;
    font-size: 104px; line-height: 118px; text-transform: uppercase;
    letter-spacing: 2px; white-space: nowrap;
  }
  .title .thin { font-weight: 200; }
  .title .bold { font-weight: 600; letter-spacing: 0; }
  .dotted-rule {
    position: absolute; left: 68px; top: 274px; width: 606px;
    border-top: 3px dotted var(--ink-muted);
  }
  .place-row {
    position: absolute; left: 68px; top: 320px; width: 606px; height: 60px;
    display: flex; align-items: center; justify-content: space-between;
  }
  .place {
    font-size: 17px; font-weight: 300; letter-spacing: 6px; text-transform: uppercase;
  }
  .wordmark {
    font-family: "Oswald", sans-serif; font-weight: 300;
    font-size: 40px; letter-spacing: 1px; color: var(--ink-light);
  }
  .club-line {
    position: absolute; left: 68px; top: 436px; width: 606px;
    font-size: 14.5px; font-weight: 400; letter-spacing: 1.5px;
    color: var(--gold); text-transform: uppercase; white-space: nowrap;
  }
  .tier {
    position: absolute; left: 68px; width: 606px;
    display: flex; align-items: center; text-align: left;
    border-bottom: 1px solid #5a5a5a; padding-bottom: 10px;
  }
  .tier-gold { top: 478px; }
  .tier-silver { top: 538px; }
  .tier-name {
    width: 190px; font-size: 21px; font-weight: 400; letter-spacing: .5px;
    text-transform: uppercase;
  }
  .tier-perks {
    list-style: none; font-family: "Arimo", sans-serif;
    font-size: 12.5px; line-height: 18px; color: var(--ink-light);
  }
  .tier-perks li::before { content: "•"; margin-right: 7px; }
  .extras {
    position: absolute; left: 68px; top: 606px; width: 606px;
    font-family: "Arimo", sans-serif; font-size: 12.5px; line-height: 20px;
    text-align: left; color: var(--ink-light);
  }
  .extras strong { font-weight: 700; }
  .website {
    position: absolute; left: 0; top: 716px; width: 742px;
    font-family: "Arimo", sans-serif; font-weight: 700;
    font-size: 12.5px; letter-spacing: 5px; text-transform: uppercase;
  }
  .tagline {
    position: absolute; left: 50px; top: 862px;
    font-family: "Oswald", sans-serif; font-weight: 300;
    font-size: 27px; line-height: 34px; letter-spacing: 1px;
    color: var(--ink-dark); text-transform: uppercase;
  }
  .footer-wordmark {
    position: absolute; left: 670px; top: 872px;
    font-family: "Oswald", sans-serif; font-weight: 300;
    font-size: 38px; color: var(--ink-dark);
  }
  .bottle-lineup { position: absolute; left: 0; top: 0; }
</style>
</head>
<body>
<main class="poster">
  <svg class="banner-shape" width="846" height="820" viewBox="0 0 846 820" aria-hidden="true">
    <polygon points="52,0 794,0 794,645 423,790 52,645" fill="var(--onyx)"/>
    <polyline points="58,662 423,805 788,662" fill="none" stroke="var(--gold)" stroke-width="7"/>
  </svg>

  <section class="banner">
    <div class="ribbon">
      <svg width="256" height="30" viewBox="0 0 256 30" aria-hidden="true">
        <polygon points="0,0 256,0 246,15 256,30 0,30 10,15" fill="var(--gold)"/>
        <line x1="18" y1="4" x2="238" y2="4" stroke="var(--gold-deep)" stroke-width="1"/>
        <line x1="18" y1="26" x2="238" y2="26" stroke="var(--gold-deep)" stroke-width="1"/>
      </svg>
      <span class="ribbon-label">Introducing</span>
    </div>

    <h1 class="title"><span class="thin">The </span><span class="bold">Onyx</span><span class="thin"> Roll</span></h1>

    <div class="dotted-rule"></div>

    <div class="place-row">
      <span class="place">Cranbrook</span>
      <span class="wordmark">Tor Ridge</span>
      <span class="place">Tasmania</span>
    </div>

    <p class="club-line">Exclusive wine club membership from the award-winning Tor Ridge estate</p>

    <div class="tier tier-gold">
      <span class="tier-name">Gold Membership:</span>
      <ul class="tier-perks">
        <li>2 cases of Tor Ridge's limited vintage (delivered May and October)</li>
        <li>receive a 15% discount</li>
      </ul>
    </div>

    <div class="tier tier-silver">
      <span class="tier-name">Silver Membership:</span>
      <ul class="tier-perks">
        <li>1 case of Tor Ridge's limited vintage (delivered May and October)</li>
        <li>receive a 10% discount</li>
      </ul>
    </div>

    <p class="extras">membership also includes exclusive access to pre-release offers &nbsp;•&nbsp; invitations to member-only tasting and events &nbsp;•&nbsp; entry into the bi-annual draw to win a 2 night stay at the Tor Weavers Cottage on the Freycinet Coast Tasmania. &nbsp;<strong>VISIT OUR WEBSITE FOR FULL DETAILS.</strong></p>

    <p class="website">www.torridgevines.com.au</p>
  </section>

  <p class="tagline">Experience<br>the taste...</p>

  <svg class="bottle-lineup" width="846" height="1200" viewBox="0 0 846 1200" role="img" aria-label="Photograph of four Tor Ridge wine bottles: two whites, one red and one rosé">
    <defs>
      <linearGradient id="white-wine" x1="0" x2="1">
        <stop offset="0" stop-color="#7c7f2a"/><stop offset=".45" stop-color="#c9c45a"/><stop offset="1" stop-color="#6d6f22"/>
      </linearGradient>
      <linearGradient id="red-wine" x1="0" x2="1">
        <stop offset="0" stop-color="#2a0509"/><stop offset=".45" stop-color="#6b1420"/><stop offset="1" stop-color="#22040a"/>
      </linearGradient>
      <linearGradient id="rose-wine" x1="0" x2="1">
        <stop offset="0" stop-color="#c25f52"/><stop offset=".45" stop-color="#f0a392"/><stop offset="1" stop-color="#b5544a"/>
      </linearGradient>
    </defs>
    <rect x="201" y="852" width="92" height="336" rx="18" fill="url(#white-wine)"/>
    <rect x="311" y="852" width="92" height="336" rx="18" fill="url(#red-wine)"/>
    <rect x="421" y="852" width="92" height="336" rx="18" fill="url(#white-wine)"/>
    <rect x="531" y="852" width="92" height="336" rx="18" fill="url(#rose-wine)"/>
  </svg>

  <span class="footer-wordmark">Tor Ridge</span>
</main>
</body>
</html>
```